Corporate travel agency website design

Hello I need a website design that will look professional. I want that anyone that gos on our site understands that we are a large successful company. I want it to be up to par with other large companies. The site should be sleek and neat.
Below I will attach my logo. A recent one page add I made and content for my add that will be used for the website.

```html
<!DOCTYPE html>
<html lang="en">
<head>
<meta charset="utf-8">
<title>Meridian Travel — Business Travel Management</title>
<link rel="stylesheet" href="https://fonts.googleapis.com/css2?family=Domine:wght@400;500&family=IBM+Plex+Sans:wght@300;400&display=swap">
<style>
:root{
  --navy:#02152f;
  --blue:#175da3;
  --accent:#1d5c8f;
  --ink:#1c1c1c;
  --muted:#5d6166;
  --mist:#eff2f3;
  --slate:#e3e6ea;
  --rule:#2a2a2a;
  --red:#e0403a;
  --white:#ffffff;
}
*{margin:0;padding:0;box-sizing:border-box}
html,body{width:1200px;height:2766px;overflow:hidden;background:var(--white)}
.page{position:relative;width:1200px;height:2766px;overflow:hidden;font-family:"IBM Plex Sans",sans-serif;font-weight:300;color:var(--muted)}
.abs{position:absolute}
.serif{font-family:"Domine",serif;font-weight:400;color:var(--ink)}

.hero-band{left:0;top:0;width:1200px;height:491px;background:var(--blue)}
.hero-shape{left:0;top:0}
.brand{left:30px;top:116px;width:220px;text-align:center;font-family:"Domine",serif;font-size:16px;letter-spacing:1.5px;color:var(--white);white-space:nowrap}
.hero-title{left:279px;top:84px;width:450px;font-size:36px;line-height:42px;letter-spacing:-.6px;white-space:nowrap;color:var(--white)}
.photo{display:block}
.photo-travellers{left:201px;top:206px;width:526px;height:350px;background:linear-gradient(135deg,#8c8f93,#c9cbcd 55%,#5b5d63)}
.photo-walker{left:744px;top:42px;width:399px;height:517px;background:linear-gradient(180deg,#6f7a86,#b8c0c7 55%,#8f969d)}
.intro{left:305px;top:603px;width:580px;font-size:17px;line-height:25.7px}

.mission-band{left:0;top:808px;width:1200px;height:722px;background:var(--mist)}
.photo-caller{left:0;top:808px;width:665px;height:450px;background:linear-gradient(120deg,#3f4650,#a7adb3 45%,#232c3d)}
.mission-card{left:424px;top:932px;width:776px;height:326px;background:var(--white)}
.mission-text{left:506px;top:1012px;width:380px;font-size:21.5px;line-height:27.5px}
.support{left:303px;top:1320px;width:510px;font-size:17px;line-height:25.7px}

.tab{left:239px;font-size:24px;line-height:30px}
.tab-active{color:var(--accent)}
.divider{left:514px;top:1576px;width:2px;height:486px;background:var(--rule)}
.marker{left:511px;top:1722px}
.detail{left:553px;top:1614px;width:400px;font-size:16.8px;line-height:25px}

.partner-band{left:0;top:2128px;width:1200px;height:572px;background:var(--slate)}
.photo-walkway{left:368px;top:2128px;width:832px;height:572px;background:linear-gradient(160deg,#c7c9cb,#eef0f1 40%,#9ea4a8 75%,#d6d8da)}
.partner-card{left:0;top:2212px;width:850px;height:445px;background:var(--white)}
.partner-title{left:239px;top:2276px;width:500px;font-size:24px;line-height:30px}
.benefits{left:239px;top:2346px;width:491px;list-style:none}
.benefit{display:flex;align-items:center;height:56.5px;border-bottom:1.5px solid var(--rule);font-size:17px;color:var(--muted)}
.benefit:last-child{border-bottom:none}
.benefit svg{width:32px;height:28px;margin:0 38px 0 12px;flex:none}
.copyright{left:239px;top:2725px;font-size:13px}
</style>
</head>
<body>
<div class="page">
  <div class="abs hero-band"></div>
  <svg class="abs hero-shape" width="1200" height="491" viewBox="0 0 1200 491"><circle cx="250" cy="50" r="390" fill="var(--navy)"/></svg>
  <div class="abs brand">MERIDIAN TRAVEL</div>
  <h1 class="abs serif hero-title" style="color:var(--white)">Get the best of business<br>travel management.</h1>
  <div class="abs photo photo-travellers" role="img" aria-label="Business travellers waiting in an airport lounge with luggage, laptop and phone"></div>
  <div class="abs photo photo-walker" role="img" aria-label="Businessman in a suit walking through a terminal pulling a suitcase"></div>
  <p class="abs intro">Meridian Travel is a global leader in business travel management services. We drive savings, efficiency, and unparalleled service to businesses and their travelers all around the world. If you are looking for a tailored travel managed solution focused on offering white glove service and fulfilling your individual preferences ,while delivering customer excellence, you’ve come to the right place.</p>

  <div class="abs mission-band"></div>
  <div class="abs photo photo-caller" role="img" aria-label="Businessman on the phone working on a laptop"></div>
  <div class="abs mission-card"></div>
  <p class="abs serif mission-text">At Meridian Travel, our mission is to have you focus on your day to day business while we handle all of the logistics and details for the most successful all encompassing travel experience.</p>
  <p class="abs support">From emergency passport arrangements to last minute cancellations, re-bookings, and other intricate travel challenges, Meridian Travel is well versed in handling the routine array of travel services, as well as solving any travel related issue that might arise.</p>

  <div class="abs serif tab" style="top:1628px">Unparalled service</div>
  <div class="abs serif tab tab-active" style="top:1703px;color:var(--accent)">Budget and Travel<br>Spend Reporting</div>
  <div class="abs serif tab" style="top:1799px;left:242px">Efficiency</div>
  <div class="abs divider"></div>
  <svg class="abs marker" width="20" height="46" viewBox="0 0 20 46"><path d="M3 0 L18 23 L3 46 Z" fill="var(--accent)"/></svg>
  <p class="abs detail">Having a travel management service will ensure that your company enforces corporate compliance and maintains control over travel decisions. This ensures that your employees stick to your budget, which in turn will protect your bottom line. Travel expenses can be costly. Having a savvy and experienced corporate travel manager who can access deep discounts not available to the public will ensure your travel is booked across the board at the lowest prices expenses are kept under control. Travel reporting is critical to optimizing budgets, streamlining expense reports, and recognizing key trends. Meridian-Travel customizes travel spend reports, by team, project, department etc, so companies can accurately track travel expenses, and make critical decisions based on the spend.</p>

  <div class="abs partner-band"></div>
  <div class="abs photo photo-walkway" role="img" aria-label="Businesswoman walking with a suitcase along a covered glass skywalk"></div>
  <div class="abs partner-card"></div>
  <h2 class="abs serif partner-title">Meridian Travel, We’re your corporate travel partner to help you manage it all.</h2>
  <ul class="abs benefits">
    <li class="benefit"><svg viewBox="0 0 32 28"><rect x="3" y="6" width="26" height="18" fill="none" stroke="var(--red)" stroke-width="1.5"/><rect x="9" y="16" width="3" height="6" fill="var(--accent)"/><rect x="14" y="13" width="3" height="9" fill="var(--accent)"/><rect x="19" y="10" width="3" height="12" fill="var(--red)"/></svg>Unparalleled savings</li>
    <li class="benefit"><svg viewBox="0 0 32 28"><rect x="14" y="2" width="9" height="8" fill="none" stroke="var(--red)" stroke-width="1.5"/><path d="M2 20 Q10 14 18 18 L28 14 Q30 16 26 19 L16 24 L4 24" fill="none" stroke="var(--accent)" stroke-width="1.6"/></svg>White globe service</li>
    <li class="benefit"><svg viewBox="0 0 32 28"><path d="M8 2 H20 L25 7 V26 H8 Z" fill="none" stroke="var(--accent)" stroke-width="1.5"/><path d="M11 10 H20 M11 14 H20 M11 18 H17" stroke="var(--accent)" stroke-width="1.3"/><circle cx="24" cy="21" r="5" fill="var(--red)"/><path d="M21.5 21 L23.5 23 L26.5 19" stroke="#fff" stroke-width="1.4" fill="none"/></svg>Corporate travel policy compliance</li>
    <li class="benefit"><svg viewBox="0 0 32 28"><circle cx="20" cy="8" r="5" fill="none" stroke="var(--red)" stroke-width="3" stroke-dasharray="2.5 1.5"/><path d="M2 22 Q10 15 18 18 L28 16 Q30 18 26 21 L16 26 L4 26 Z" fill="var(--accent)"/></svg>Full service travel management</li>
    <li class="benefit"><svg viewBox="0 0 32 28"><rect x="7" y="2" width="18" height="24" fill="none" stroke="var(--red)" stroke-width="1.5"/><circle cx="16" cy="9" r="3.5" fill="none" stroke="var(--accent)" stroke-width="1.3"/><path d="M11 22 V18 M15 22 V16 M19 22 V19" stroke="var(--accent)" stroke-width="1.8"/></svg>Streamlined expense reports</li>
  </ul>
  <div class="abs serif copyright">Copyright © Meridiantravel.com</div>
</div>
</body>
</html>
```